Postcard Design

Law office.
Details are on the attached pdf file:
NOTE: the following items are to be changed, as follows:
1. price is 799
2. delete "Expires 2-8-13"
3. make "Nevada County's..." into "Northern California's ... "
4. Someplace where it fits nicely, add "Fast, Easy, Done!"
5. Delete "no obligation first visit"
6. That attached pdf was a successful ad so I want to maintain that look GENERALLY, but I'm not stuck on anything in particular. Some freedom to play with it for a perfect ad.
7. I'll attach the revised picture and the logo.

```html
<!DOCTYPE html>
<html lang="en">
<head>
<meta charset="UTF-8">
<title>Law Office of Daniel R. Marlow – Estate Plans Postcard</title>
<link href="https://fonts.googleapis.com/css2?family=Cabin:ital,wght@0,400;0,600;0,700;1,400&display=swap" rel="stylesheet">
<style>
  :root {
    --navy: #2f3f95;
    --navy-light: #4a5cb0;
    --violet: #544f9b;
    --lime: #c3d33c;
    --lime-text: #b6cb22;
    --lime-band: #d8e36a;
    --lime-faint: #c2cd5c;
    --white: #ffffff;
    --photo-top: #a7abac;
    --photo-bottom: #5f6467;
  }
  * { box-sizing: border-box; margin: 0; padding: 0; }
  html, body { width: 1200px; height: 900px; overflow: hidden; background: var(--white); }
  body { font-family: "Cabin", "Gill Sans", sans-serif; }
  .postcard { position: relative; width: 1200px; height: 900px; background: var(--white); }

  .headline-band {
    position: absolute; left: 0; top: 58px; width: 1200px; height: 45px;
    background: linear-gradient(90deg, var(--navy) 0%, var(--navy-light) 50%, var(--navy) 100%);
    color: var(--white); text-align: center;
    font-size: 45px; line-height: 45px; font-weight: 600; letter-spacing: 0.5px;
  }
  .headline-band strong { font-weight: 700; }

  .pitch { position: absolute; left: 20px; width: 680px; text-align: center; }
  .pitch-protect { top: 190px; color: var(--lime-text); font-size: 44px; font-weight: 700; }
  .pitch-call { top: 250px; color: var(--navy); font-size: 37px; font-weight: 400; }
  .pitch-done { top: 380px; color: var(--navy); font-size: 38px; font-weight: 700; letter-spacing: 5px; }

  .offer-box {
    position: absolute; left: 737px; top: 127px; width: 438px; height: 380px;
    background: var(--violet); border-radius: 22px; color: var(--white); text-align: center;
  }
  .offer-items { margin-top: 12px; font-size: 33px; font-weight: 700; line-height: 45px; }
  .offer-price { color: var(--lime); font-size: 134px; font-weight: 700; line-height: 140px; margin-top: 6px; }
  .offer-value { font-size: 28px; font-style: italic; margin-top: 14px; }

  .identity-band {
    position: absolute; left: 0; top: 532px; width: 1200px; height: 264px; background: var(--lime-band);
  }
  .brand-mark {
    position: absolute; left: 26px; top: 14px; width: 190px; height: 236px;
    border: 3px solid var(--lime-faint); display: flex; align-items: center; justify-content: center;
    color: var(--lime-faint); font-size: 44px; font-weight: 600;
  }
  .firm { position: absolute; left: 230px; width: 705px; text-align: center; color: var(--navy); }
  .firm-label { top: 34px; font-size: 32px; font-weight: 400; }
  .firm-name { top: 100px; font-size: 66px; font-weight: 700; }
  .firm-tagline { top: 195px; font-size: 25px; font-weight: 600; }
  .firm-tagline em { font-weight: 400; }
  .dot { display: inline-block; width: 7px; height: 7px; border-radius: 50%; background: var(--navy); margin: 0 12px 5px; }

  .attorney-photo {
    position: absolute; left: 968px; top: 15px; width: 210px; height: 234px; border-radius: 10px;
    background: radial-gradient(ellipse at 50% 35%, var(--photo-top), var(--photo-bottom));
  }

  .contact-band {
    position: absolute; left: 0; top: 796px; width: 1200px; height: 48px; background: var(--navy);
    color: var(--white); text-align: center; font-size: 31px; line-height: 46px; font-weight: 400;
  }
  .contact-band .phone { font-weight: 700; letter-spacing: 2px; }
  .contact-band .web { text-decoration: underline; text-underline-offset: 4px; }
  .contact-band .dot { background: var(--white); width: 8px; height: 8px; margin: 0 14px 6px; }
</style>
</head>
<body>
<main class="postcard">
  <header class="headline-band">Northern California’s <strong>Best</strong> in Estate Plans</header>

  <p class="pitch pitch-protect">Protect Your Loved Ones!</p>
  <p class="pitch pitch-call">It’s Easy- Call Now!</p>
  <p class="pitch pitch-done">FAST, EASY, DONE!</p>

  <section class="offer-box">
    <p class="offer-items">Living Trusts,<br>Wills, &amp; All Necessary<br>Documents</p>
    <p class="offer-price">$799</p>
    <p class="offer-value">Over $2,000 Value</p>
  </section>

  <section class="identity-band">
    <div class="brand-mark">Marlow</div>
    <p class="firm firm-label">Law Office of</p>
    <h1 class="firm firm-name">Daniel R. Marlow</h1>
    <p class="firm firm-tagline">Thousands Served<span class="dot"></span><em>Since 1998</em></p>
    <div class="attorney-photo" role="img" aria-label="Portrait photo of the attorney in a dark suit and tie"></div>
  </section>

  <footer class="contact-band">
    Free Notarization<span class="dot"></span><span class="phone">(530)-555-0147</span><span class="dot"></span><span class="web">www.DanielMarlowLaw.com</span>
  </footer>
</main>
</body>
</html>
```